Fitness business need 3x3 card to promote 6wk boot camp nutrition challenge

Hi, we're looking for someone to make our current card look better and more modern. We want to keep the text the same, but we want a better design. We also want to keep the woman on the front of the card. The card is for both men and women so we want it to feel inclusive and bright. The idea is to make the card look more modern. We want some pops of color. The main feature is to promote the pricing on the back of the card. It would be nice if that continues to look like a coupon or if it stands out with a bright color or background.

Target Market(s)

Men and women looking to get in shape

Industry/Entity Type

Fitness

Font styles to use
Serif
Sans Serif

Colors
3176b5
0255a3
33a6d7
f37122
ec1f27

Requirements
Must have
• front and back, use pic of women provided

```html
<!DOCTYPE html>
<html lang="en">
<head>
<meta charset="utf-8">
<title>6 Week Boot Camp Nutrition Challenge – Card Front and Back</title>
<link rel="stylesheet" href="https://fonts.googleapis.com/css2?family=Bebas+Neue&family=Oswald:wght@300;400&family=Montserrat:wght@600&display=swap">
<style>
  :root {
    --sky: #33a6d7;
    --orange: #f37122;
    --ink: #2b2f36;
    --paper: #e9e9e9;
    --white: #ffffff;
    --stage: #f2f2f2;
  }
  * { box-sizing: border-box; margin: 0; padding: 0; }
  html, body { width: 1200px; height: 663px; overflow: hidden; }
  body { background: var(--stage); position: relative; }

  .card {
    position: absolute;
    top: 72px;
    width: 486px;
    height: 486px;
    background: var(--sky);
    overflow: hidden;
    box-shadow: 0 6px 16px rgba(0,0,0,0.18);
  }
  .card--front { left: 80px; }
  .card--back { left: 634px; }

  .band { position: absolute; left: 0; width: 100%; background: var(--paper); }
  .band--top { top: 0; height: 50px; }
  .band--bottom { bottom: 0; height: 33px; }
  .band svg { position: absolute; left: 0; top: 0; width: 100%; height: 100%; }

  .display { font-family: "Bebas Neue", "Oswald", sans-serif; font-weight: 400; }
  .accent { color: var(--orange); }
  .dark { color: var(--ink); }

  .brand-tab {
    position: absolute;
    background: var(--orange);
    color: var(--white);
    font-family: "Bebas Neue", sans-serif;
    font-size: 36px;
    line-height: 1;
    display: flex;
    align-items: center;
    justify-content: flex-end;
  }
  .card--front .brand-tab {
    top: 8px; right: 0; width: 222px; height: 72px;
    padding-right: 18px;
    clip-path: polygon(0 0, 100% 0, 100% 100%, 22% 100%);
  }
  .card--back .brand-tab {
    bottom: 0; right: 0; width: 220px; height: 74px;
    padding-right: 22px;
    clip-path: polygon(18% 0, 100% 0, 100% 100%, 0 100%);
  }

  .photo {
    position: absolute;
    top: 50px; left: 0; width: 486px; height: 403px;
    background: linear-gradient(160deg, #cfcfcf 0%, #9a9a9a 45%, #4a4a4a 100%);
    clip-path: polygon(196px 0, 486px 0, 486px 403px, 392px 403px);
  }

  .front-headline {
    position: absolute;
    left: 24px; top: 84px;
    font-size: 37px;
    line-height: 38px;
    color: var(--white);
  }
  .dates {
    position: absolute;
    left: 24px; top: 256px;
    display: flex;
    align-items: flex-start;
    gap: 14px;
    color: var(--white);
  }
  .dates svg { width: 30px; height: 34px; margin-top: 6px; }
  .dates p {
    font-family: "Oswald", sans-serif;
    font-weight: 300;
    font-size: 25px;
    line-height: 31px;
  }

  .url {
    position: absolute;
    font-family: "Montserrat", sans-serif;
    font-weight: 600;
    color: var(--white);
  }
  .card--front .url { left: 29px; top: 420px; font-size: 14px; }
  .card--back .url { left: 45px; top: 430px; font-size: 12.5px; }

  .back-headline {
    position: absolute;
    top: 74px; left: 0; width: 100%;
    text-align: center;
    font-size: 40px;
    line-height: 44px;
    color: var(--white);
  }
  .benefits {
    position: absolute;
    top: 134px; left: 0; width: 100%; height: 104px;
    background: var(--orange);
    color: var(--white);
    font-family: "Oswald", sans-serif;
    font-weight: 300;
    font-size: 21px;
    line-height: 30px;
    text-align: center;
    padding-top: 7px;
  }

  .price-badge {
    position: absolute;
    left: 40px; top: 258px;
    width: 164px; height: 164px;
  }
  .price-badge svg { position: absolute; inset: 0; width: 100%; height: 100%; }
  .price-badge__text {
    position: absolute; inset: 0;
    display: flex; flex-direction: column; align-items: center; justify-content: center;
    font-family: "Bebas Neue", sans-serif;
    line-height: 1;
  }
  .price-badge__amount { color: var(--white); font-size: 58px; margin-top: 4px; }
  .price-badge__term { color: var(--orange); font-size: 24px; margin-top: 2px; }

  .back-title {
    position: absolute;
    right: 24px; top: 272px;
    text-align: right;
    font-size: 44px;
    line-height: 44px;
    color: var(--white);
  }
</style>
</head>
<body>

<section class="card card--front" aria-label="Card front">
  <div class="band band--top">
    <svg viewBox="0 0 486 50" preserveAspectRatio="none" aria-hidden="true">
      <polygon points="0,0 78,0 104,50 0,50" fill="var(--orange)"/>
      <polygon points="96,0 112,0 138,50 122,50" fill="var(--orange)"/>
      <polygon points="128,0 146,0 172,50 154,50" fill="var(--orange)"/>
    </svg>
  </div>

  <div class="photo" role="img" aria-label="Black-and-white photo of a woman sitting on the floor, resting her arm on a medicine ball"></div>

  <div class="brand-tab">BRANDNAME</div>

  <h1 class="front-headline display">
    <span class="accent">6WEEK</span> BOOT<br>
    CAMP NUTRITION<br>
    <span class="accent">CHALLENGE</span>
  </h1>

  <div class="dates">
    <svg viewBox="0 0 30 34" aria-hidden="true">
      <polyline points="3,3 14,17 3,31" fill="none" stroke="var(--white)" stroke-width="4"/>
      <polyline points="15,3 26,17 15,31" fill="none" stroke="var(--white)" stroke-width="4"/>
    </svg>
    <p>October 2nd<br>to November 11th</p>
  </div>

  <p class="url">www.fitcampsix.com</p>

  <div class="band band--bottom">
    <svg viewBox="0 0 486 33" preserveAspectRatio="none" aria-hidden="true">
      <polygon points="300,0 318,0 338,33 320,33" fill="var(--orange)"/>
      <polygon points="332,0 350,0 370,33 352,33" fill="var(--orange)"/>
      <polygon points="364,0 486,0 486,33 384,33" fill="var(--orange)"/>
    </svg>
  </div>
</section>

<section class="card card--back" aria-label="Card back">
  <div class="band band--top">
    <svg viewBox="0 0 486 50" preserveAspectRatio="none" aria-hidden="true">
      <polygon points="0,26 92,26 104,50 0,50" fill="var(--orange)"/>
      <polygon points="98,26 114,26 126,50 110,50" fill="var(--orange)"/>
      <polygon points="130,26 148,26 160,50 142,50" fill="var(--orange)"/>
    </svg>
  </div>

  <h2 class="back-headline display">
    <span class="dark">NO</span> BARBELLS! <span class="dark">NO</span> HEAVY WEIGHTS!
  </h2>

  <div class="benefits">
    <p>Burn fat, build muscle &amp; have fun!</p>
    <p>Tons of classes led by world-class coaches.</p>
    <p>Personalized nutrition planning, prizes, and more!</p>
  </div>

  <div class="price-badge">
    <svg viewBox="-82 -82 164 164" aria-hidden="true">
      <defs>
        <radialGradient id="badge-fill" cx="40%" cy="35%" r="70%">
          <stop offset="0" stop-color="#3a3d42"/>
          <stop offset="1" stop-color="#15171a"/>
        </radialGradient>
      </defs>
      <g fill="url(#badge-fill)">
        <circle r="72"/>
        <circle cy="-72" r="9"/>
        <circle cy="-72" r="9" transform="rotate(15)"/>
        <circle cy="-72" r="9" transform="rotate(30)"/>
        <circle cy="-72" r="9" transform="rotate(45)"/>
        <circle cy="-72" r="9" transform="rotate(60)"/>
        <circle cy="-72" r="9" transform="rotate(75)"/>
        <circle cy="-72" r="9" transform="rotate(90)"/>
        <circle cy="-72" r="9" transform="rotate(105)"/>
        <circle cy="-72" r="9" transform="rotate(120)"/>
        <circle cy="-72" r="9" transform="rotate(135)"/>
        <circle cy="-72" r="9" transform="rotate(150)"/>
        <circle cy="-72" r="9" transform="rotate(165)"/>
        <circle cy="-72" r="9" transform="rotate(180)"/>
        <circle cy="-72" r="9" transform="rotate(195)"/>
        <circle cy="-72" r="9" transform="rotate(210)"/>
        <circle cy="-72" r="9" transform="rotate(225)"/>
        <circle cy="-72" r="9" transform="rotate(240)"/>
        <circle cy="-72" r="9" transform="rotate(255)"/>
        <circle cy="-72" r="9" transform="rotate(270)"/>
        <circle cy="-72" r="9" transform="rotate(285)"/>
        <circle cy="-72" r="9" transform="rotate(300)"/>
        <circle cy="-72" r="9" transform="rotate(315)"/>
        <circle cy="-72" r="9" transform="rotate(330)"/>
        <circle cy="-72" r="9" transform="rotate(345)"/>
      </g>
    </svg>
    <div class="price-badge__text">
      <span class="price-badge__amount">$249</span>
      <span class="price-badge__term">6WEEKS</span>
    </div>
  </div>

  <h2 class="back-title display">
    <span class="dark">6WEEK</span> BOOT<br>
    CAMP NUTRITION<br>
    <span class="dark">CHALLENGE</span>
  </h2>

  <p class="url">www.fitcampsix.com</p>

  <div class="band band--bottom"></div>
  <div class="brand-tab">BRANDNAME</div>
</section>

</body>
</html>
```